■ 依頼の目的/概要

老人ホームの封筒デザインを依頼させて頂きます。
・A4封筒
・事務用封筒窓付き(B4三つ折り)

■ 封筒に記載する情報

施設名・住所・電話・fax・URL

〒358-0642
花咲県緑野市下川原412
TEL027-280-3000
FAX027-280-3003
URL http://www.hanasato-kai.jp

```html
<!DOCTYPE html>
<html lang="ja">
<head>
<meta charset="utf-8">
<title>花里の郷 封筒デザイン</title>
<link rel="stylesheet" href="https://fonts.googleapis.com/css2?family=Noto+Sans+JP:wght@400;500;700&display=swap">
<style>
  :root {
    --paper: #ffffff;
    --backdrop: #ffffff;
    --edge: #d9d9d9;
    --flap-blue: #17b3e6;
    --flap-teal: #2fc1b0;
    --flap-green: #8cc63f;
    --brand-green: #3fa535;
    --brand-blue: #1d7fc4;
    --text-main: #555555;
    --text-soft: #9a9a9a;
    --decor: #dfe9c4;
  }
  * { margin: 0; padding: 0; box-sizing: border-box; }
  html, body {
    width: 849px; height: 1200px; overflow: hidden;
    background: var(--backdrop);
    font-family: "Noto Sans JP", sans-serif;
  }
  .envelope {
    position: absolute; left: 62px; top: 57px;
    width: 725px; height: 1076px;
    background: var(--paper);
    border: 1px solid var(--edge);
  }
  .envelope__flap {
    position: absolute; left: -1px; top: -1px;
    width: 727px; height: 96px;
  }
  .sender {
    position: absolute; left: 62px; bottom: 48px;
    color: var(--text-main);
  }
  .sender__brand {
    display: flex; align-items: center; gap: 14px;
    margin-bottom: 14px;
  }
  .sender__badge {
    width: 40px; height: 40px; border-radius: 50%;
    background: var(--brand-green);
  }
  .sender__name {
    font-size: 44px; font-weight: 700; line-height: 1;
    color: var(--brand-blue); letter-spacing: 0.04em;
  }
  .sender__address {
    font-size: 11px; color: var(--text-soft);
    letter-spacing: 0.05em; margin-bottom: 6px;
  }
  .sender__contacts {
    display: flex; align-items: baseline; gap: 22px;
    font-size: 10px; color: var(--text-soft);
    white-space: nowrap;
  }
  .sender__tel {
    font-size: 19px; font-weight: 500; color: var(--text-main);
  }
  .sender__tel small { font-size: 10px; margin-right: 4px; }
  .envelope__decor {
    position: absolute; right: 70px; bottom: 40px;
    width: 150px; height: 150px; border-radius: 50%;
    background: var(--decor); opacity: 0.6;
  }
</style>
</head>
<body>
  <div class="envelope">
    <svg class="envelope__flap" viewBox="0 0 727 96" aria-hidden="true">
      <defs>
        <linearGradient id="flapGradient" x1="0" y1="0" x2="1" y2="0">
          <stop offset="0" stop-color="#17b3e6"/>
          <stop offset="0.5" stop-color="#2fc1b0"/>
          <stop offset="1" stop-color="#8cc63f"/>
        </linearGradient>
      </defs>
      <polygon points="0,0 727,0 727,14 712,96 15,96 0,14" fill="url(#flapGradient)"/>
    </svg>

    <div class="envelope__decor" aria-hidden="true"></div>

    <div class="sender">
      <div class="sender__brand">
        <span class="sender__badge" aria-hidden="true"></span>
        <span class="sender__name">花里の郷</span>
      </div>
      <p class="sender__address">〒358-0642　花咲県緑野市下川原412</p>
      <div class="sender__contacts">
        <span class="sender__tel"><small>TEL.</small>049-615-7200</span>
        <span>FAX. 049-615-7204</span>
        <span>URL. http://www.hanasato-kai.jp</span>
      </div>
    </div>
  </div>
</body>
</html>
```